"Vine Hollow Excursions" is a top notch Santa Barbara County Wine Tour company.

We provide scenic, boutique and custom wine tours. I need the card to be clean and classy. I will provide our logo. I would like the logo to cover the back side of the card as an option and would like to see a couple color options other then our signature green and gold. I would like to see some creative options and let the designers come up with options.
I need cards for myself and my team. The final design should communicate "An authentic and boutique wine tour experience"
Please use my website for reference www.vinehollowexcursions.example

Target Market(s)

We have a wide range of clients from millennials to baby boomers

Industry/Entity Type

Tour

Contact Information for Business Card

Contact info:
Dale Morrow
805-291-6382
info@vinehollowexcursions.example
vinehollowexcursions.example

Colors

Designer to choose colors to be used in the design.

Requirements
Must have
• my logo
Nice to have
• *I would like to have the backside side with the logo and the company statement
• "An authentic and boutique wine tour experience" as an option.
• *I would also like to see what the designers can create!
• *I would like to see an option that incorporates or social: snapgrid, chirpa, route scout
Should not have
• I do not want it too busy.

```html
<!DOCTYPE html>
<html lang="en">
<head>
<meta charset="utf-8">
<title>Vine Hollow Excursions — Business Card</title>
<link href="https://fonts.googleapis.com/css2?family=Cinzel:wght@400&family=Lora:wght@400&display=swap" rel="stylesheet">
<style>
  :root {
    --backdrop: #2a2a2a;
    --vine-green: #28664a;
    --paper: #ffffff;
    --gold-deep: #a3714c;
    --gold-light: #dcbb9c;
    --ink-green: #2a6a48;
  }
  * { box-sizing: border-box; margin: 0; padding: 0; }
  html, body {
    width: 1189px; height: 1200px; overflow: hidden;
    background: var(--backdrop);
  }
  .card {
    position: absolute; left: 166px; width: 856px; height: 489px;
    border-radius: 26px;
  }
  .card--front { top: 66px; background: var(--vine-green); }
  .card--back { top: 626px; background: var(--paper); }

  .front-brand {
    position: absolute; left: 0; right: 0; top: 200px;
    text-align: center; color: #fff;
    font-family: "Cinzel", serif; font-weight: 400;
    font-size: 46px; letter-spacing: 2px; line-height: 1;
  }
  .front-tagline {
    position: absolute; left: 0; right: 0; top: 410px;
    text-align: center; color: #fff;
    font-family: "Lora", serif; font-size: 18px; letter-spacing: 4.3px;
  }

  .back-brand {
    position: absolute; left: 40px; width: 330px; top: 205px;
    text-align: center; color: var(--gold-deep);
    font-family: "Cinzel", serif; font-weight: 400;
    font-size: 30px; line-height: 1.15; letter-spacing: 1px;
  }
  .divider {
    position: absolute; left: 407px; top: 186px; width: 2px; height: 164px;
    background: linear-gradient(var(--gold-light), var(--gold-deep), var(--gold-light));
  }
  .contact { position: absolute; left: 467px; top: 182px; }
  .contact-name {
    font-family: "Cinzel", serif; font-size: 27px; letter-spacing: 0.5px;
    background: linear-gradient(90deg, var(--gold-deep), var(--gold-light) 60%, var(--gold-deep));
    -webkit-background-clip: text; background-clip: text; color: transparent;
    margin-bottom: 8px;
  }
  .contact-line {
    display: flex; align-items: center; gap: 8px;
    font-family: "Lora", serif; font-size: 17px; color: var(--ink-green);
    height: 27px;
  }
  .contact-line svg { width: 24px; height: 24px; flex: none; }
  .social {
    display: flex; flex-wrap: wrap; gap: 6px 14px; width: 330px; margin-top: 12px;
  }
  .social-item {
    display: flex; align-items: center; gap: 5px;
    font-family: "Lora", serif; font-size: 13px; color: var(--ink-green);
  }
  .social-item::before {
    content: ""; width: 12px; height: 12px; border-radius: 50%;
    border: 1.5px solid var(--ink-green);
  }
</style>
</head>
<body>
  <section class="card card--front">
    <div class="front-brand">Vine Hollow<br>Excursions</div>
    <p class="front-tagline">An authentic boutique wine tour experience</p>
  </section>

  <section class="card card--back">
    <div class="back-brand">Vine Hollow<br>Excursions</div>
    <div class="divider"></div>
    <div class="contact">
      <div class="contact-name">Dale Morrow</div>
      <div class="contact-line">
        <svg viewBox="0 0 24 24" fill="none" stroke="var(--ink-green)" stroke-width="1.6"><circle cx="12" cy="12" r="10.5"/><path d="M7 10c0-2 2-3 5-3s5 1 5 3l-2 1-1-2h-4l-1 2zM8 12h8v4H8z" fill="var(--ink-green)" stroke="none"/></svg>
        805-291-6382
      </div>
      <div class="contact-line">
        <svg viewBox="0 0 24 24" fill="none" stroke="var(--ink-green)" stroke-width="1.6"><circle cx="12" cy="12" r="10.5"/><rect x="7" y="8.5" width="10" height="7" fill="var(--ink-green)" stroke="none"/><path d="M7 8.5l5 4 5-4" stroke="#fff" stroke-width="1.2"/></svg>
        info@vinehollowexcursions.example
      </div>
      <div class="contact-line">
        <svg viewBox="0 0 24 24" fill="none" stroke="var(--ink-green)" stroke-width="1.4"><circle cx="12" cy="12" r="10.5"/><circle cx="12" cy="12" r="6"/><ellipse cx="12" cy="12" rx="2.5" ry="6"/><path d="M6 12h12"/></svg>
        vinehollowexcursions.example
      </div>
      <div class="social">
        <span class="social-item">route scout</span>
        <span class="social-item">snapgrid</span>
        <span class="social-item">chirpa</span>
        <span class="social-item">hearthbook</span>
        <span class="social-item">chatterly</span>
      </div>
    </div>
  </section>
</body>
</html>
```